Investigation Tool App - Static Google Ad Image

We need a static image design that promotes our website, which provides an online incident investigation collaboration tool. I would like this static image for Google, but I am also seeking the same design in a LinkedIn Ad ratio.

We would like to see engaging ad graphics that capture the essence of collaboration, time saving, fast "impact-to-learnings" type vibe. As it helps them collaborate and facilitate the investigation on our interactive canvas and then it has an automated report builder that is AI-assisted to turn their information into coherent sentences in the report, it is not fully AI generated (this is important as i feel people inherently distrust AI generated content).

This tool is aimed at safety professionals in mining, construction and oil & gas who want an easy way to facilitate investigations virtually or in person without having to use whiteboards and double handle information and that want to be able to generate a report and learnings on the same day to quickly prevent further harm.

I have included a bunch of snips of my site and features etc - please feel free to use any of them but dont be constrained by these.

Target Market(s)

Safety Professionals/ Managers in Mining, Oil & Gas & Construction

Industry/Entity Type

Mining, Oil & Gas & Construction

Font styles to use
Sans Serif

Requirements
Nice to have
• Modern, pain point focussed, visual of investigation map and or nodes
Should not have
• No em-dashes, no gimmicky language or terms

```html
<!DOCTYPE html>
<html lang="en">
<head>
<meta charset="UTF-8">
<title>From Incident to Insight, in One Day</title>
<link rel="stylesheet" href="https://fonts.googleapis.com/css2?family=Archivo+Black&family=Poppins:wght@400;500;600&family=Inter:wght@400;500;600;700&display=swap">
<style>
  :root {
    --ink: #141a2b;
    --white: #ffffff;
    --brand-blue: #2f6be9;
    --device-dark: #141414;
    --device-silver: #c9cbcf;
    --ui-border: #d6d8dc;
    --ui-grey: #eef0f2;
    --ui-text: #3a3f48;
    --link-blue: #3d8bd9;
    --map-light: #f4f7f8;
    --map-mid: #e3eef0;
  }
  * { box-sizing: border-box; margin: 0; padding: 0; }
  html, body { width: 1200px; height: 1200px; overflow: hidden; }
  body { background: var(--white); font-family: "Poppins", sans-serif; }

  .ad {
    position: relative;
    width: 1200px;
    height: 1200px;
    overflow: hidden;
    background: var(--white);
  }
  .ad__band { position: absolute; inset: 0; }
  .ad__headline {
    position: absolute;
    top: 44px;
    left: 0;
    width: 100%;
    text-align: center;
    font-family: "Archivo Black", sans-serif;
    font-weight: 400;
    font-size: 80px;
    line-height: 96px;
    letter-spacing: 1px;
    color: var(--ink);
  }
  .ad__subline {
    position: absolute;
    top: 240px;
    left: 0;
    width: 100%;
    text-align: center;
    font-family: "Poppins", sans-serif;
    font-size: 38px;
    line-height: 53px;
    color: var(--ink);
  }
  .ad__tagline {
    position: absolute;
    top: 1120px;
    left: 0;
    width: 100%;
    text-align: center;
    font-family: "Inter", sans-serif;
    font-weight: 500;
    font-size: 39px;
    letter-spacing: 0.3px;
    color: var(--white);
  }

  /* Laptop */
  .laptop__lid {
    position: absolute;
    left: 139px;
    top: 441px;
    width: 915px;
    height: 606px;
    background: var(--device-dark);
    border-radius: 26px 26px 0 0;
    border: 2px solid #3a3a3a;
  }
  .laptop__camera {
    position: absolute;
    top: 9px;
    left: 50%;
    width: 8px; height: 8px;
    margin-left: -4px;
    border-radius: 50%;
    background: #2b2b2b;
  }
  .laptop__screen {
    position: absolute;
    left: 25px;
    top: 34px;
    right: 25px;
    bottom: 30px;
    background: var(--white);
    overflow: hidden;
  }
  .laptop__base {
    position: absolute;
    left: 33px;
    top: 1043px;
    width: 1129px;
    height: 30px;
    border-radius: 4px 4px 40px 40px;
    background: linear-gradient(#e6e7e9, var(--device-silver) 60%, #8f9196);
  }
  .laptop__notch {
    position: absolute;
    left: 50%;
    top: 0;
    width: 150px;
    height: 10px;
    margin-left: -75px;
    border-radius: 0 0 10px 10px;
    background: #a9abb0;
  }

  /* PDF preview UI */
  .preview__bar {
    height: 44px;
    display: flex;
    align-items: center;
    justify-content: space-between;
    padding: 0 10px 0 12px;
    border-bottom: 1px solid var(--ui-border);
    font-family: "Inter", sans-serif;
  }
  .preview__title { font-size: 11px; font-weight: 600; color: var(--ui-text); }
  .preview__actions { display: flex; gap: 4px; }
  .preview__button {
    font-size: 9px;
    padding: 6px 8px;
    border: 1px solid #b8bbc1;
    border-radius: 2px;
    color: var(--ui-text);
    background: var(--white);
  }
  .preview__button--active { background: #4a4d52; color: var(--white); border-color: #4a4d52; }
  .preview__body {
    position: absolute;
    top: 44px; left: 0; right: 0; bottom: 0;
    background: var(--ui-grey);
    padding: 10px 28px 0 12px;
  }
  .preview__scroll {
    position: absolute;
    right: 10px; top: 56px;
    width: 6px; height: 330px;
    border-radius: 3px;
    background: #9a9da3;
  }
  .page {
    position: relative;
    height: 100%;
    background: var(--white);
    padding: 0 0 0 30px;
  }
  .page__header {
    display: flex;
    align-items: center;
    justify-content: space-between;
    height: 44px;
    padding-right: 24px;
    font-family: "Inter", sans-serif;
  }
  .page__brand { display: flex; align-items: center; gap: 12px; }
  .page__brand-name { font-size: 17px; font-weight: 700; color: #111; letter-spacing: 0.5px; }
  .page__brand-label { font-size: 9px; font-weight: 600; color: var(--link-blue); letter-spacing: 1px; }
  .page__doc { font-size: 9.5px; font-weight: 600; color: var(--ui-text); }
  .page__map {
    position: absolute;
    left: 49px;
    top: 62px;
    width: 700px;
    height: 306px;
    border: 1px solid #e2e3e6;
    background: radial-gradient(ellipse at 55% 50%, var(--map-mid), var(--map-light) 70%);
  }
</style>
</head>
<body>
<main class="ad">
  <svg class="ad__band" width="1200" height="1200" viewBox="0 0 1200 1200" aria-hidden="true">
    <polygon points="0,970 1200,453 1200,1200 0,1200" fill="var(--brand-blue)"/>
  </svg>

  <h1 class="ad__headline">FROM INCIDENT TO<br>INSIGHT, IN ONE DAY</h1>
  <p class="ad__subline">Collaborate on a shared canvas and generate clear,<br>structured reports, fast.</p>

  <div class="laptop">
    <div class="laptop__lid">
      <span class="laptop__camera"></span>
      <div class="laptop__screen">
        <div class="preview__bar">
          <span class="preview__title">PDF Preview</span>
          <div class="preview__actions">
            <span class="preview__button">Vertical</span>
            <span class="preview__button preview__button--active">Horizontal</span>
            <span class="preview__button">Save / Print</span>
            <span class="preview__button">Close</span>
          </div>
        </div>
        <div class="preview__body">
          <div class="page">
            <div class="page__header">
              <div class="page__brand">
                <span class="page__brand-name">Northline</span>
                <span class="page__brand-label">SYSTEM MAP</span>
              </div>
              <span class="page__doc">Document Name: Falling Objects - Bow Tie Map</span>
            </div>
            <div class="page__map" role="img" aria-label="Bow tie investigation map of a falling object incident, with threat, control and recovery nodes joined by connector lines"></div>
          </div>
          <span class="preview__scroll"></span>
        </div>
      </div>
    </div>
    <div class="laptop__base"><span class="laptop__notch"></span></div>
  </div>

  <p class="ad__tagline">AI-ASSISTED REPORTING. HUMAN-LED INSIGHTS.</p>
</main>
</body>
</html>
```